Kelvane Plumbing Business cards

Company is Kelvane Plumbing.
name Dashel Morrowby, I am a plumber, drainer, gasfitter and roofer
Mobile: 0431 906 154
Email address: info@kelvaneplumbing.example (check out my website for some ideas)
Website: www.kelvaneplumbing.example
ABN: 82 916 203 471
LIC: 604517K

I am reliable all round plumber. I am a 24 hour emergency service. Kelvane Plumbing is a professional plumbing service in the Illawarra, South Coast, Southern Sydney and Southern Highland regions of NSW. We offer a 24 hour emergency service for piece of mind to our customers. Call us now to see how we can help you. Kelvane Plumbing approaches every job with attention to detail and excellent customer service. With our superior workmanship you can be confident that the job will be done right the first time around. You can rest assured with results that are guaranteed to last.

Target Market(s)

the general public

Contact Information for Business Card

look up website for some ideas something with similar colours to logo and new modern and to catch the eye.

Colors
fdfdfd
ffffff
000000
7f7f7f
aaaaaa
33a6d7
0492cd

Requirements
Must have
• all contact details
• company- Kelvane Plumbing
• name- Dashel Morrowby
• number mobile- 0431 906 154
• Email address- info@kelvaneplumbing.example
• Website- www.kelvaneplumbing.example
• ABN- 82 916 203 471
• LIC- 604517K

```html
<!DOCTYPE html>
<html lang="en">
<head>
<meta charset="utf-8">
<title>Kelvane Plumbing – Business Cards</title>
<link rel="stylesheet" href="https://fonts.googleapis.com/css2?family=Ubuntu:wght@400;500;700&display=swap">
<style>
  :root {
    --bg: #d9d9d9;
    --card: #050505;
    --blue: #0492cd;
    --blue-soft: #33a6d7;
    --grey: #7f7f7f;
    --white: #fdfdfd;
  }
  * { margin: 0; padding: 0; box-sizing: border-box; }
  html, body { width: 1200px; height: 1200px; overflow: hidden; }
  body { background: var(--bg); font-family: "Ubuntu", sans-serif; position: relative; }

  .card {
    position: absolute;
    width: 964px; height: 579px;
    background: var(--card);
    box-shadow: 0 6px 18px rgba(0,0,0,.35);
  }
  .card--front { left: 68px; top: 12px; }
  .card--back { left: 176px; top: 606px; }

  .centered { position: absolute; transform: translate(-50%, -50%); white-space: nowrap; text-align: center; }

  .brand-mark { display: flex; flex-direction: column; align-items: center; gap: 10px; }
  .brand-mark__dot { width: 22px; height: 22px; border-radius: 50%; background: var(--blue-soft); }
  .brand-mark__name { color: var(--blue-soft); font-weight: 500; font-size: 26px; }

  .company-name { color: var(--blue); font-weight: 700; font-size: 42px; letter-spacing: -0.5px; text-transform: uppercase; }
  .company-tag { color: var(--grey); font-size: 28px; letter-spacing: 0.5px; }

  .divider { position: absolute; left: 496px; top: 148px; width: 4px; height: 330px; background: var(--blue); }

  .person-name { position: absolute; left: 527px; top: 148px; transform: translateY(-50%); color: var(--blue); font-weight: 700; font-size: 39px; white-space: nowrap; }
  .person-role { color: var(--white); font-size: 22px; }

  .contact { position: absolute; left: 558px; display: flex; align-items: center; color: var(--white); font-size: 23px; transform: translateY(-50%); white-space: nowrap; }
  .contact__icon { width: 30px; height: 28px; margin-right: 9px; display: flex; align-items: center; justify-content: center; color: var(--blue); font-size: 30px; font-weight: 700; }
  .contact__label { color: var(--blue); }
  .contact--meta .contact__label { margin-right: 6px; }
</style>
</head>
<body>

<section class="card card--front">
  <div class="centered brand-mark" style="left:482px; top:249px;">
    <span class="brand-mark__dot"></span>
    <span class="brand-mark__name">Kelvane Plumbing</span>
  </div>
  <h1 class="centered company-name" style="left:482px; top:374px;">Kelvane Plumbing</h1>
  <p class="centered company-tag" style="left:482px; top:423px;">company</p>
</section>

<section class="card card--back">
  <div class="centered brand-mark" style="left:276px; top:255px;">
    <span class="brand-mark__dot"></span>
    <span class="brand-mark__name">Kelvane Plumbing</span>
  </div>
  <h2 class="centered company-name" style="left:276px; top:380px;">Kelvane Plumbing</h2>
  <p class="centered company-tag" style="left:276px; top:431px;">company</p>

  <div class="divider"></div>

  <h3 class="person-name">DASHEL MORROWBY</h3>
  <p class="centered person-role" style="left:716px; top:198px;">plumber, drainer, gasfitter</p>

  <div class="contact" style="top:325px;">
    <span class="contact__icon">
      <svg width="30" height="28" viewBox="0 0 30 28" fill="none" stroke="currentColor" stroke-width="3" stroke-linecap="round">
        <path d="M8 3 H5 Q2 3 2 7 V21 Q2 25 5 25 H8 V19 H6 V9 H8 Z" fill="currentColor" stroke-width="1.5"/>
        <path d="M13 10 Q15 14 13 18" stroke-width="2"/>
        <path d="M17 7 Q21 14 17 21" stroke-width="2"/>
        <path d="M21 4 Q27 14 21 24" stroke-width="2"/>
      </svg>
    </span>
    <span>0431 906 154</span>
  </div>
  <div class="contact" style="top:362px;">
    <span class="contact__icon">@</span>
    <span>info@kelvaneplumbing.example</span>
  </div>
  <div class="contact" style="top:399px;">
    <span class="contact__icon">
      <svg width="28" height="28" viewBox="0 0 28 28" fill="none" stroke="currentColor" stroke-width="2.5">
        <circle cx="14" cy="14" r="11.5"/>
        <ellipse cx="14" cy="14" rx="5" ry="11.5"/>
        <line x1="2.5" y1="14" x2="25.5" y2="14"/>
        <line x1="5" y1="7.5" x2="23" y2="7.5"/>
        <line x1="5" y1="20.5" x2="23" y2="20.5"/>
      </svg>
    </span>
    <span>www.kelvaneplumbing.example</span>
  </div>
  <div class="contact contact--meta" style="top:440px; left:558px;">
    <span class="contact__label">ABN</span><span>- 82 916 203 471</span>
  </div>
  <div class="contact contact--meta" style="top:471px; left:558px;">
    <span class="contact__label">LIC</span><span>- &nbsp;604517K</span>
  </div>
</section>

</body>
</html>
```